依頼詳細
現在使用しているデザインとロゴデータをアップしておきます。
・色は「青」をつかったデザインでお願いします。下地の色は白でも色ありでも構いません。
・事業内容である太陽光パネルを想起させるようなモチーフ的なものを取り入れたいです。
・英語表記については あってもなくてもどちらでも構いません。
・主に一般顧客向けの営業をしております。名刺を渡す相手も個人向けがほとんどです。
・紙質については、ボード紙やコットンペーパーなど厚みがあるものが理想です。デザインをいただくにあたり、どのような紙質を想定されたデザインかなどもあわせてご提案いただけると幸いです。
記載項目
会社名 会社電話番号 会社住所 支店住所 HPアドレス
氏名 携帯番号 メールアドレス
希望イメージ
シンプル 複雑
単色 カラフル
暗い 明るい
日常 高級
遊び心 厳粛
未来的 伝統的
女性的 男性的
希望する色
青系
納品ファイル
• イラストレーター形式 (.ai)
• PNG形式 (.png)
補足説明

依頼内容をしっかりと把握いただき理解いただいた上での提案だったので。

素敵なデザインありがとうございます。とても気に入りました。

```html
<!DOCTYPE html>
<html lang="ja">
<head>
<meta charset="utf-8">
<title>名刺デザイン 入稿シート</title>
<link rel="stylesheet" href="https://fonts.googleapis.com/css2?family=Noto+Sans+JP:wght@400;500;700&display=swap">
<style>
  :root {
    --sheet: #ffffff;
    --ink: #2b2f36;
    --ink-soft: #555b66;
    --brand: #2d6fb8;
    --card-top: #ffffff;
    --card-bottom: #b9d2ee;
    --mark: #8a8f96;
    --guide: #c9ccd1;
    --heaven: #f4a640;
    --earth: #7cbf4a;
  }
  * { box-sizing: border-box; margin: 0; padding: 0; }
  html, body { width: 867px; height: 1200px; overflow: hidden; background: var(--sheet); }
  body { position: relative; font-family: "Noto Sans JP", sans-serif; color: var(--ink); }

  .trim-label {
    position: absolute; left: 18px; font-size: 13px; color: var(--mark);
    writing-mode: vertical-rl; letter-spacing: 2px;
  }
  .trim-label.side { writing-mode: horizontal-tb; left: 8px; }

  .marks { position: absolute; left: 0; top: 0; width: 867px; height: 1200px; pointer-events: none; }

  .face-tag {
    position: absolute; width: 44px; height: 36px; border: 1.5px solid var(--ink);
    font-size: 22px; text-align: center; line-height: 32px; background: #fff;
  }
  .dot {
    position: absolute; width: 26px; height: 26px; border-radius: 50%;
    font-size: 13px; text-align: center; line-height: 26px; color: #fff; font-weight: 700;
  }
  .dot.heaven { background: var(--heaven); }
  .dot.earth { background: var(--earth); }
  .dim { position: absolute; font-size: 12px; color: var(--mark); }

  .card {
    position: absolute; left: 160px; width: 606px; height: 372px;
    background: linear-gradient(180deg, var(--card-top) 0%, var(--card-top) 22%, var(--card-bottom) 100%);
  }
  .card.front { top: 168px; }
  .card.back { top: 768px; }

  .brand { position: absolute; left: 34px; top: 34px; display: flex; align-items: center; gap: 10px; }
  .brand-dot { width: 26px; height: 26px; border-radius: 50%; background: var(--heaven); }
  .brand-text { display: flex; flex-direction: column; }
  .brand-kana { font-size: 9px; color: var(--brand); margin-left: 60px; }
  .brand-name { font-size: 27px; font-weight: 500; color: var(--brand); letter-spacing: 2px; line-height: 1.1; }

  .person { position: absolute; left: 40px; top: 150px; font-size: 11px; line-height: 1.7; color: var(--ink-soft); }
  .person .name { font-size: 26px; font-weight: 500; color: var(--ink); letter-spacing: 6px; margin-top: 30px; padding-left: 50px; }

  .offices { position: absolute; left: 330px; top: 108px; font-size: 11px; line-height: 1.55; color: var(--ink-soft); }
  .offices .gap { height: 10px; }

  .business-line { position: absolute; left: 32px; right: 32px; top: 326px; font-size: 9px; line-height: 1.6; color: var(--ink-soft); text-align: center; }

  .back .role { position: absolute; left: 190px; top: 150px; font-size: 12px; font-weight: 700; }
  .back .name-en { position: absolute; left: 190px; top: 166px; font-size: 26px; font-weight: 700; letter-spacing: 1px; }
  .back .offices-en { position: absolute; left: 40px; top: 218px; font-size: 9.5px; line-height: 1.55; color: var(--ink-soft); }
  .back .offices-en b { color: var(--ink); font-weight: 700; }
  .back .offices-en .gap { height: 6px; }
  .back .web { position: absolute; left: 0; right: 0; top: 340px; text-align: center; font-size: 12px; font-weight: 700; }
</style>
</head>
<body>

<svg class="marks" viewBox="0 0 867 1200" aria-hidden="true">
  <g stroke="var(--mark)" stroke-width="1" fill="none">
    <!-- front sheet crop marks -->
    <rect x="148" y="156" width="630" height="396" stroke="var(--guide)"/>
    <path d="M160 120 V150 M766 120 V150 M160 570 V600 M766 570 V600 M110 168 H140 M110 540 H140 M786 168 H816 M786 540 H816"/>
    <path d="M148 120 V150 M778 120 V150 M148 570 V600 M778 570 V600 M110 156 H140 M110 552 H140 M786 156 H816 M786 552 H816"/>
    <path d="M463 120 V150 M463 570 V600 M110 354 H140 M786 354 H816" stroke="var(--guide)"/>
    <path d="M170 138 H440 M500 138 H756"/>
    <path d="M800 180 V320 M800 390 V530"/>
    <path d="M60 100 V150 M60 150 L54 140 M60 150 L66 140 M30 165 H100 M100 165 L90 159 M100 165 L90 171"/>
    <!-- back sheet crop marks -->
    <rect x="148" y="756" width="630" height="396" stroke="var(--guide)"/>
    <path d="M160 720 V750 M766 720 V750 M160 1160 V1190 M766 1160 V1190 M110 768 H140 M110 1140 H140 M786 768 H816 M786 1140 H816"/>
    <path d="M148 720 V750 M778 720 V750 M148 1160 V1190 M778 1160 V1190 M110 756 H140 M110 1152 H140 M786 756 H816 M786 1152 H816"/>
    <path d="M463 720 V750 M463 1160 V1190 M110 954 H140 M786 954 H816" stroke="var(--guide)"/>
    <path d="M30 765 H100 M100 765 L90 759 M100 765 L90 771"/>
  </g>
</svg>

<div class="trim-label" style="top:20px;">仕上がり線</div>
<div class="trim-label side" style="top:140px;">仕上がり線</div>
<div class="trim-label side" style="top:740px;">仕上がり線</div>

<div class="dim" style="left:448px; top:130px;">91mm</div>
<div class="dim" style="left:808px; top:345px;">55mm</div>

<div class="dot heaven" style="left:650px; top:124px;">天</div>
<div class="face-tag" style="left:690px; top:118px;">表</div>
<div class="dot earth" style="left:450px; top:560px;">地</div>

<div class="dot heaven" style="left:650px; top:724px;">天</div>
<div class="face-tag" style="left:690px; top:718px;">表</div>
<div class="dot earth" style="left:450px; top:1160px;">地</div>

<section class="card front">
  <div class="brand">
    <span class="brand-dot"></span>
    <div class="brand-text">
      <span class="brand-kana">株式会社 ソラブルージャパン</span>
      <span class="brand-name">SOLA BLUE JAPAN</span>
    </div>
  </div>

  <div class="person">
    <div>営業統括部</div>
    <div>住宅用太陽光アドバイザー　登録番号 0000000</div>
    <div class="name">青山　拓海</div>
  </div>

  <div class="offices">
    <div>【本社】</div>
    <div>〒060-0807</div>
    <div>北海道札幌市中央区北七条西5-2-8 ソラビル3F</div>
    <div>TEL. 011-555-0142 / FAX. 011-555-0143</div>
    <div>携帯 090-5555-0168</div>
    <div>mail : t.aoyama@solablue-example.jp</div>
    <div class="gap"></div>
    <div>【仙台支店】</div>
    <div>〒980-0014</div>
    <div>宮城県仙台市青葉区本町4-6-12 青葉第2ビル</div>
    <div>TEL. 022-555-0187</div>
  </div>

  <div class="business-line">
    太陽光発電システム・蓄電池の販売施工／オール電化リフォーム／省エネ住宅のご相談<br>
    電気工事業　登録番号 0000000
  </div>
</section>

<section class="card back">
  <div class="brand">
    <span class="brand-dot"></span>
    <div class="brand-text">
      <span class="brand-kana">株式会社 ソラブルージャパン</span>
      <span class="brand-name">SOLA BLUE JAPAN</span>
    </div>
  </div>

  <div class="role">COO</div>
  <div class="name-en">Takumi AOYAMA</div>

  <div class="offices-en">
    <div><b>[HEAD OFFICE]</b></div>
    <div>Sola Bldg. 3F, 5-2-8 Kita 7-jo Nishi, Chuo-ku, Sapporo-shi, Hokkaido 060-0807</div>
    <div>TEL: +81(0)11-555-0142 / FAX: +81(0)11-555-0143</div>
    <div>cellar phone : +81(0)90-5555-0168 / e-mail : t.aoyama@solablue-example.jp</div>
    <div class="gap"></div>
    <div><b>[SENDAI BRANCH]</b></div>
    <div>Aoba 2nd Bldg., 4-6-12 Honcho, Aoba-ku, Sendai-shi, Miyagi 980-0014</div>
    <div>TEL: +81(0)22-555-0187</div>
  </div>

  <div class="web">www.solablue-example.jp</div>
</section>

</body>
</html>
```